Tobrin Pelmo Broth is looking for a DL Flyer for their unique food the #velmorabroth

We're looking for a punchy flyer which depicts our food dish and includes a small blurb on the front & back. Flyer size is portrait style DL (210 x 99mm) & must be 'Press Ready Files'.
Brief: Flyer background is light wooden chopping board with vertical strips.

(Text: Calibri Body or similar text, must be easy to read! Minimum 50% width)
TvR proudly present..
(Text: Calibri Body Header or similar text, must be easy to read! Min. 75% width) PELMO BROTH

Below the text PELMO BROTH insert an image (size is approx 25% of Flyer) of Borneo with a reference to Kuching. Map of Borneo can be an outline or similar but not too prominent.
Overlay the top of the map with the following text in Monotype Corsivab or similar! but must be easy to read.
Text: Kuching (2 sizes larger) Capital City of Sarawak on the Island of Borneo is home to some of the world’s greatest and unique dishes.
(new line) TvR will take you on a culinary journey to Kuching with a favourite local dish the
(new line) #VelmoraBroth (double space) so sit back, relax & enjoy!

Insert and centre the attached image DSC_0927.JPG
Remove the spoon and make the image more vibrant, do not change the colour of the soup.
Refer to attached file Flyer.jpg for images of chopsticks, a boiled egg and ingredients at the bottom. We like the lines to point to key ingredients e.g. to the egg, prawns etc. current design the font is difficult to read.

List contact details toward the bottom.
e: TvR.PelmoBroth@quillmail.example
m: +61 437152096
f : Tobrin Pelmo Broth

on the reverse of the Flyer:
Background is light wooden chopping board with vertical strips, same as front.

Refer to below link for text & Nutritional Values table.
The text for the main four paragraphs should be the key note and majority.
Note the Ingredients and the Nutritional Values table size is max 12.5% of the total Flyer size.

https://files.dorvanshare.example/doc/7QmTx83LwPzR2nVb5KcYe0HsJd4UfAi6Go1tNr9/edit

Target Market(s)

An international foody with a sense of adventure. The dish is nutritional, Gluten Free and a healthy meal. It will be sold at food markets, to office workers for lunch and for a lighter evening meal.

Industry/Entity Type

Food Production

Colors

Designer to choose colors to be used in the design.

Requirements
Must have
• 'TvR proudly present..' must be a statement along with the product 'PELMO BROTH'
• The map of Borneo with reference to Kuching, the home of the product.
• A picture of the dish itself.

```html
<!DOCTYPE html>
<html lang="en">
<head>
<meta charset="utf-8">
<title>Tobrin Pelmo Broth – DL Flyer</title>
<link href="https://fonts.googleapis.com/css2?family=Open+Sans:wght@400;600;700;800&family=Cormorant+Garamond:ital,wght@1,500;1,600&display=swap" rel="stylesheet">
<style>
  :root {
    --page: #ece7de;
    --paper: #ffffff;
    --board-light: #e3d3a0;
    --board-mid: #d6c286;
    --board-dark: #c9b274;
    --ink: #5b3f1e;
    --ink-soft: #7a5a33;
    --map: rgba(125, 92, 45, 0.28);
    --band: rgba(110, 78, 40, 0.78);
    --band-solid: #7d5b34;
    --accent: #e2502a;
    --white: #ffffff;
  }
  * { box-sizing: border-box; margin: 0; padding: 0; }
  html, body { width: 1200px; height: 844px; overflow: hidden; }
  body {
    background: var(--page);
    font-family: "Open Sans", Arial, sans-serif;
    color: var(--ink);
    position: relative;
  }
  .flyer {
    position: absolute;
    top: 30px;
    width: 370px;
    height: 784px;
    background: var(--paper);
    box-shadow: 0 4px 14px rgba(0,0,0,0.12);
  }
  .flyer--front { left: 180px; }
  .flyer--back { left: 650px; }
  .board {
    position: absolute;
    inset: 12px;
    border-radius: 18px;
    overflow: hidden;
    background:
      repeating-linear-gradient(90deg,
        rgba(255,255,255,0.10) 0 9px,
        rgba(120,90,40,0.06) 9px 11px,
        rgba(255,255,255,0.04) 11px 23px,
        rgba(120,90,40,0.09) 23px 24px,
        rgba(255,255,255,0.08) 24px 37px),
      linear-gradient(90deg, var(--board-mid), var(--board-light) 45%, var(--board-dark));
  }
  .handle-slot {
    position: absolute;
    top: 14px;
    width: 160px;
    height: 34px;
    background: var(--paper);
    border-radius: 17px;
  }
  .flyer--front .handle-slot { left: 16px; }
  .flyer--back .handle-slot { right: 20px; top: 44px; }

  /* front */
  .presents {
    position: absolute; top: 58px; left: 0; right: 0;
    text-align: center; font-weight: 700; font-size: 21px; color: var(--ink);
  }
  .product-title {
    position: absolute; top: 82px; left: 0; right: 0;
    text-align: center; font-weight: 800; font-size: 44px; letter-spacing: 1px;
    color: var(--ink-soft);
  }
  .borneo-map {
    position: absolute; top: 150px; left: 110px; width: 200px; height: 140px;
    background: var(--map);
    border-radius: 48% 52% 40% 60% / 55% 45% 55% 45%;
    transform: rotate(-12deg);
  }
  .intro { position: absolute; top: 140px; left: 20px; right: 20px; text-align: center; }
  .intro__city {
    font-family: "Cormorant Garamond", Georgia, serif; font-style: italic; font-weight: 600;
    font-size: 19px; letter-spacing: 1px; color: var(--ink);
  }
  .intro__lead {
    font-family: "Cormorant Garamond", Georgia, serif; font-style: italic; font-weight: 500;
    font-size: 12.5px; line-height: 1.2; color: var(--ink);
  }
  .pin-label {
    position: absolute; top: 196px; left: 38px;
    display: flex; align-items: center; gap: 3px;
    font-size: 8px; font-weight: 700; color: var(--accent);
  }
  .journey {
    position: absolute; top: 212px; left: 22px; right: 22px;
    text-align: center; font-weight: 700; font-size: 14px; line-height: 1.28; color: var(--ink);
  }
  .dish-photo {
    position: absolute; top: 312px; left: 58px; width: 256px; height: 256px;
    border-radius: 50%;
    background: radial-gradient(circle, #b4502a 0 42%, #d98a4a 56%, #f5efe6 64%, #ffffff 72%);
  }
  .callouts { position: absolute; inset: 0; pointer-events: none; }
  .callout {
    position: absolute; font-weight: 800; font-size: 10px; line-height: 0.95;
    color: var(--ink); text-align: center; text-transform: uppercase;
  }
  .callout--chicken { top: 280px; left: 26px; }
  .callout--beancurd { top: 330px; left: 14px; }
  .callout--egg { top: 470px; left: 12px; }
  .callout--prawns { top: 488px; right: 10px; }
  .callout--sprouts { top: 576px; right: 64px; }
  .ingredients-photo {
    position: absolute; left: 0; top: 540px; width: 120px; height: 220px;
    background: linear-gradient(160deg, rgba(220,215,200,0) 0%, #b9c98a 30%, #6f9a3d 55%, #c8a46a 80%, #a4754a 100%);
    border-top-right-radius: 60px;
  }
  .contact-band {
    position: absolute; left: 0; right: 0; top: 648px; height: 86px;
    background: var(--band);
    padding: 10px 14px 0 60px;
  }
  .contact-row {
    display: flex; justify-content: flex-end; align-items: center; gap: 7px;
    color: var(--white); font-weight: 700; font-size: 12px; line-height: 23px;
    white-space: nowrap;
  }
  .contact-row svg { flex: none; }

  /* back */
  .story {
    position: absolute; top: 88px; left: 22px; right: 22px; text-align: center;
    font-weight: 700; font-size: 12.6px; line-height: 1.26; color: var(--ink);
  }
  .story__head { font-weight: 800; font-size: 13.5px; margin-bottom: 2px; }
  .story p + p { margin-top: 8px; }
  .ingredients-list {
    position: absolute; top: 560px; left: 22px; right: 22px; text-align: center;
    font-size: 10px; line-height: 1.2; color: var(--ink);
  }
  .ingredients-list strong { font-weight: 800; }
  .nutrition {
    position: absolute; top: 626px; left: 16px; right: 16px;
    border-collapse: collapse; font-size: 10.5px; font-weight: 700; color: var(--white);
  }
  .nutrition th, .nutrition td { padding: 1px 8px; text-align: left; text-transform: uppercase; }
  .nutrition thead th { background: var(--band-solid); line-height: 1.1; }
  .nutrition thead th.serve { text-transform: none; text-align: center; background: #6a4a27; }
  .nutrition tbody th { color: var(--white); background: rgba(110,78,40,0.55); border-top: 1px solid rgba(255,255,255,0.6); }
  .nutrition tbody td { background: var(--band-solid); border-top: 1px solid rgba(255,255,255,0.6); width: 42%; }
</style>
</head>
<body>

<section class="flyer flyer--front" aria-label="Flyer front">
  <div class="board">
    <div class="handle-slot"></div>

    <p class="presents">TvR proudly presents..</p>
    <h1 class="product-title">PELMO BROTH</h1>

    <div class="borneo-map" role="img" aria-label="Faint outline map of Borneo marking Kuching"></div>

    <div class="intro">
      <p class="intro__city">KUCHING</p>
      <p class="intro__lead">Capital City of Sarawak on the Island of Borneo<br>is home to some of the world's greatest and unique dishes.</p>
    </div>

    <div class="pin-label">
      KUCHING
      <svg width="9" height="12" viewBox="0 0 9 12" aria-hidden="true"><path d="M4.5 0C2 0 0 2 0 4.4 0 7.6 4.5 12 4.5 12S9 7.6 9 4.4C9 2 7 0 4.5 0z" fill="#e2502a"/><circle cx="4.5" cy="4.4" r="1.7" fill="#fff"/></svg>
    </div>

    <p class="journey">TvR will take you on a culinary journey to Kuching with a favourite local dish the #VelmoraBroth&nbsp;&nbsp;so sit back, relax &amp; enjoy!</p>

    <div class="dish-photo" role="img" aria-label="Bowl of broth with rice vermicelli, omelette strips, chicken, king prawns, bean curd, half boiled egg, coriander and chopsticks"></div>

    <svg class="callouts" width="346" height="760" viewBox="0 0 346 760" aria-hidden="true">
      <g fill="none" stroke="#3e2a12" stroke-width="1.3">
        <path d="M62 312 C85 320 150 318 178 332"/>
        <path d="M40 360 C60 372 80 382 100 390"/>
        <path d="M42 492 C56 472 80 450 96 446"/>
        <path d="M318 486 C300 476 262 464 236 458"/>
        <path d="M282 578 C250 568 222 548 212 528"/>
      </g>
      <g fill="#3e2a12">
        <circle cx="178" cy="332" r="2.5"/>
        <circle cx="100" cy="390" r="2.5"/>
        <circle cx="96" cy="446" r="2.5"/>
        <circle cx="236" cy="458" r="2.5"/>
        <circle cx="212" cy="528" r="2.5"/>
      </g>
    </svg>
    <p class="callout callout--chicken">Sliced<br>Chicken<br>Breast</p>
    <p class="callout callout--beancurd">Fried<br>Bean<br>Curd</p>
    <p class="callout callout--egg">Free<br>Range<br>Egg</p>
    <p class="callout callout--prawns">King<br>Prawns</p>
    <p class="callout callout--sprouts">Bean<br>Sprouts</p>

    <div class="ingredients-photo" role="img" aria-label="Fresh ingredients: spring onion, garlic, ginger, fried bean curd and chilli"></div>

    <div class="contact-band">
      <p class="contact-row">TvR.PelmoBroth@quillmail.example
        <svg width="13" height="10" viewBox="0 0 13 10" aria-hidden="true"><rect x="0.6" y="0.6" width="11.8" height="8.8" fill="none" stroke="#fff" stroke-width="1.2"/><path d="M0.6 0.6 6.5 5.5 12.4 0.6" fill="none" stroke="#fff" stroke-width="1.2"/></svg>
      </p>
      <p class="contact-row">+61 437152096
        <svg width="13" height="13" viewBox="0 0 13 13" aria-hidden="true"><rect x="2.6" y="0.6" width="7.8" height="11.8" rx="1.2" fill="none" stroke="#fff" stroke-width="1.2"/><circle cx="6.5" cy="10.3" r="0.8" fill="#fff"/></svg>
      </p>
      <p class="contact-row">Tobrin Pelmo Broth
        <svg width="13" height="11" viewBox="0 0 13 11" aria-hidden="true"><rect x="1" width="11" height="11" rx="1.5" fill="#fff"/></svg>
      </p>
    </div>
  </div>
</section>

<section class="flyer flyer--back" aria-label="Flyer back">
  <div class="board">
    <div class="handle-slot"></div>

    <div class="story">
      <p class="story__head">EATS MALAYSIA:</p>
      <p>A short while ago on my travels around East Malaysia I was introduced to a place called Kuching, Capital City of Sarawak. I was overwhelmed by their number of unique dishes, from the Sea to the Borneo Jungle local sustainable ingredients are sourced to create some of Kuching's indigenous foods.</p>
      <p>I was astonished to learn that famous Kuching dishes like Kolo Mee and the Sarawak Laksa are breakfast dishes and often sold out by 10am.</p>
      <p>I have chosen the Sarawak Laksa to share with You.. It converts perfectly to our requirements - a healthy, Gluten-Free nourishing meal, although maybe not breakfast for everyone!</p>
      <p>The Laksa sambal / base stock is made from ALL plant-based ingredients. We add a dash of coconut milk to bring balance to this simple yet complex dish; with it's more subtle and fine blend of aromatic herbs and spices and a hint of sour and chilli undertones.</p>
    </div>

    <p class="ingredients-list"><strong>Ingredients:</strong> rice vermicelli - bihoon, omelette strips (free range eggs), sliced chicken breast, King prawns, bean-sprouts, fried bean curd and garnished with lime wedge, fresh coriander and sambal on the side.</p>

    <table class="nutrition">
      <thead>
        <tr><th>Nutrition Information:</th><th class="serve">Pelmo Broth<br>Per Serve</th></tr>
      </thead>
      <tbody>
        <tr><th>Energy</th><td>1920kJ</td></tr>
        <tr><th>Calories</th><td>458</td></tr>
        <tr><th>Protein</th><td>30g</td></tr>
        <tr><th>&nbsp;&nbsp;-Gluten</th><td>Undetected</td></tr>
        <tr><th>Fat - Total</th><td>38g</td></tr>
        <tr><th>Carbohydrates</th><td>52g</td></tr>
      </tbody>
    </table>
  </div>
</section>

</body>
</html>
```